Corporate Branding - Web and Print

A UK based company will like to use an existing logo to create branding materials for all marketing related documents, including business card, prints, letterhead, Website, Twitter, Facebook, Instagram logo etc. This company serves high-end clientele in the fashion, health and wellness and as such high quality and class is of utmost importance.
Where the logo can be modernised without losing its character then experiment. The main thing is to have a corporate branding which can be used later for brochures, Business Plan infographics.
The prominent colour within the organisation is burnt orange with no secondary colour. However if you believe a secondary colour is needed then use it, otherwise keep it simple and classy. Any chosen colours have to match perfectly.
Target Market(s)
High net worth individuals
Industry/Entity Type
Health And Wellness
Contact Information for Business Card
classy
Look and feel
Each slider illustrates characteristics of the customer's brand and the style your logo design should communicate.

```html
<!DOCTYPE html>
<html lang="en">
<head>
<meta charset="utf-8">
<title>Velmora – Business Card</title>
<link rel="stylesheet" href="https://fonts.googleapis.com/css2?family=Source+Sans+3:wght@400;600;700&display=swap">
<style>
  :root {
    --backdrop: #3a3a3a;
    --card: #050909;
    --orange: #f7941d;
    --white: #f4f4f4;
  }
  html, body {
    margin: 0;
    padding: 0;
    overflow: hidden;
  }
  body {
    width: 1200px;
    height: 864px;
    background: var(--backdrop);
    position: relative;
    font-family: "Source Sans 3", sans-serif;
  }
  .card {
    position: absolute;
    top: 312px;
    width: 419px;
    height: 239px;
    background: var(--card);
    border-radius: 14px;
    box-shadow: 0 4px 10px rgba(0,0,0,0.45);
  }
  .card--front { left: 171px; }
  .card--back { left: 609px; }

  .brand {
    position: absolute;
    left: 45px;
    top: 80px;
    width: 150px;
    text-align: center;
  }
  .brand__dot {
    width: 38px;
    height: 38px;
    border-radius: 50%;
    background: var(--orange);
    margin: 0 auto 6px;
  }
  .brand__name {
    color: var(--orange);
    font-weight: 700;
    font-size: 25px;
    letter-spacing: 1px;
    line-height: 1;
  }

  .divider {
    position: absolute;
    left: 212px;
    top: 70px;
    width: 1.5px;
    height: 80px;
    background: var(--orange);
  }
  .info {
    position: absolute;
    left: 227px;
    top: 70px;
    color: var(--white);
  }
  .info__name {
    color: var(--orange);
    font-size: 17px;
    font-weight: 600;
    line-height: 1.1;
    margin: 0;
  }
  .info__title {
    font-size: 11.5px;
    margin: 1px 0 14px;
  }
  .contact {
    list-style: none;
    margin: 0;
    padding: 0;
    font-size: 11.5px;
    line-height: 14.5px;
  }
  .contact li {
    display: flex;
    align-items: center;
    gap: 5px;
  }
  .contact svg {
    width: 8px;
    height: 8px;
    flex: none;
  }

  .back-brand {
    position: absolute;
    left: 0;
    right: 0;
    top: 82px;
    text-align: center;
  }
  .back-brand__dot {
    width: 76px;
    height: 76px;
    border-radius: 50%;
    background: var(--orange);
    margin: 0 auto 8px;
  }
  .back-brand__name {
    color: var(--orange);
    font-weight: 700;
    font-size: 16px;
    letter-spacing: 1px;
  }
  .back-web {
    position: absolute;
    left: 0;
    right: 0;
    top: 205px;
    text-align: center;
    color: var(--white);
    font-size: 11.5px;
  }
</style>
</head>
<body>
  <section class="card card--front">
    <div class="brand">
      <div class="brand__dot"></div>
      <div class="brand__name">VELMORA</div>
    </div>
    <div class="divider"></div>
    <div class="info">
      <p class="info__name">Clara Hale</p>
      <p class="info__title">President</p>
      <ul class="contact">
        <li>
          <svg viewBox="0 0 10 10"><path d="M2 0.5 L4 2.5 L3 3.8 Q4.5 6 6.2 7 L7.5 6 L9.5 8 L8 9.5 Q3.5 9 0.5 2 Z" fill="var(--orange)"/></svg>
          01 020-555-0143
        </li>
        <li>
          <svg viewBox="0 0 10 10"><rect x="2.5" y="0.5" width="5" height="9" rx="1" fill="none" stroke="var(--orange)" stroke-width="1.2"/></svg>
          01 020-555-0187
        </li>
        <li>
          <svg viewBox="0 0 10 10"><rect x="0.5" y="2" width="9" height="6" fill="var(--orange)"/><path d="M0.5 2 L5 5.5 L9.5 2" fill="none" stroke="var(--card)" stroke-width="0.8"/></svg>
          hello@velmorawell.com
        </li>
        <li>
          <svg viewBox="0 0 10 10"><circle cx="5" cy="5" r="4.3" fill="none" stroke="var(--orange)" stroke-width="1"/><path d="M0.7 5 H9.3 M5 0.7 V9.3" stroke="var(--orange)" stroke-width="0.8"/></svg>
          velmorawell.com
        </li>
      </ul>
    </div>
  </section>

  <section class="card card--back">
    <div class="back-brand">
      <div class="back-brand__dot"></div>
      <div class="back-brand__name">VELMORA</div>
    </div>
    <div class="back-web">www.velmorawell.com</div>
  </section>
</body>
</html>
```